I need a business card to launch my business. I am a carpenter who works with wood and metal framing. I do commercial and residential properties. I do the final fixtures in expensive residential properties. For example custom made wardrobes, prefinished doors and skirtings. I have an eye for detail and take pride in my work.

I don't want to be pigeon holed as a guy with a tool belt and a hammer. I want to look like a professional company. I want my logo to be modern and young and edgy. I don't have any preference for colours but don't want yellow.

Industry/Entity Type

Residential

Contact Information for Business Card

Cedar Line Carpentry
specialising in residential and commercial fit outs

Mark Dolan
Phone: 0413 528 036
cedarlinecarpentry@mailbrook.com

Logo styles of interest
Pictorial/Combination Logo
Wordmark Logo
Lettermark Logo

```html
<!DOCTYPE html>
<html lang="en">
<head>
<meta charset="utf-8">
<title>Cedar Line Carpentry – Business Card</title>
<link href="https://fonts.googleapis.com/css2?family=Montserrat:wght@700&family=Open+Sans:wght@400;600&display=swap" rel="stylesheet">
<style>
  :root {
    --page-bg: #e9e6e1;
    --card-white: #ffffff;
    --maroon: #7a1518;
    --maroon-dark: #5a0d10;
    --gold: #c9b27a;
    --tagline: #8a2a2c;
    --light-text: #ffffff;
  }
  html, body {
    margin: 0;
    padding: 0;
    width: 1200px;
    height: 1023px;
    overflow: hidden;
    background: var(--page-bg);
  }
  .card {
    position: absolute;
    left: 150px;
    top: 254px;
    width: 900px;
    height: 514px;
    background: var(--card-white);
    box-shadow: 0 10px 30px rgba(0,0,0,0.18);
    overflow: hidden;
    font-family: "Open Sans", Arial, sans-serif;
  }
  .card-shapes {
    position: absolute;
    inset: 0;
  }
  .brand {
    position: absolute;
    left: 110px;
    top: 128px;
    width: 420px;
  }
  .brand-name {
    margin: 0;
    font-family: "Montserrat", Arial, sans-serif;
    font-weight: 700;
    font-size: 54px;
    line-height: 1.05;
    color: var(--maroon);
    text-transform: uppercase;
    letter-spacing: -0.5px;
  }
  .brand-tagline {
    margin: 14px 0 0;
    font-size: 12px;
    font-weight: 400;
    color: var(--tagline);
    text-transform: uppercase;
    letter-spacing: 0.3px;
  }
  .contact-block {
    position: absolute;
    left: 476px;
    top: 400px;
    display: flex;
    align-items: center;
    color: var(--light-text);
  }
  .person-name {
    font-size: 14px;
    font-weight: 400;
    text-transform: uppercase;
    letter-spacing: 0.5px;
    white-space: nowrap;
  }
  .divider {
    width: 1px;
    height: 50px;
    background: var(--gold);
    margin: 0 16px;
  }
  .contact-list {
    margin: 0;
    padding: 0;
    list-style: none;
    font-size: 14px;
    line-height: 1.75;
    white-space: nowrap;
  }
  .contact-label {
    display: inline-block;
    width: 16px;
    color: var(--gold);
    font-weight: 600;
  }
</style>
</head>
<body>
  <div class="card">
    <svg class="card-shapes" width="900" height="514" viewBox="0 0 900 514" aria-hidden="true">
      <defs>
        <linearGradient id="bandShade" x1="0" y1="0" x2="1" y2="0">
          <stop offset="0" stop-color="#8c1c20"/>
          <stop offset="1" stop-color="#5a0d10"/>
        </linearGradient>
      </defs>
      <path d="M 140 514 Q 560 430 725 0" fill="none" stroke="#c9b27a" stroke-width="9"/>
      <path d="M 180 514 Q 600 440 760 0 L 900 0 L 900 514 Z" fill="url(#bandShade)"/>
    </svg>

    <div class="brand">
      <h1 class="brand-name">Cedar Line<br>Carpentry</h1>
      <p class="brand-tagline">Specialising in residential and commercial</p>
    </div>

    <div class="contact-block">
      <div class="person-name">Mark Dolan</div>
      <div class="divider"></div>
      <ul class="contact-list">
        <li><span class="contact-label">P</span>0413 528 036</li>
        <li><span class="contact-label">E</span>cedarlinecarpentry@mailbrook.com</li>
      </ul>
    </div>
  </div>
</body>
</html>
```